Flyer design needed for services offered and to show reviews from previous customers

I would like a Flyer designed showing some of the services i offer:
-LED lighting upgrades (pot lights, accent & commercial)
-Electrical repairs & Service work
- Fayglowen lighting
- TV wall mounts
My website is Voltarisa.ca if you need any photos from there in higher quality please let me know and i can provide them.

I want it to have a couple reviews from previous customers (attached links to facebook and google page)
Google:
https://revpage.example/r/QZ8kd4mtpWhaJXo/review
Facebook:
https://www.socialbook.example/Voltarisa-Contracting-Ltd-552918730461283

```html
<!DOCTYPE html>
<html lang="en">
<head>
<meta charset="utf-8">
<title>Voltarisa Contracting – Services Flyer</title>
<link href="https://fonts.googleapis.com/css2?family=Barlow+Condensed:wght@500;600;700&family=Barlow+Semi+Condensed:wght@600&family=Barlow:wght@600&family=Montserrat:wght@400;600&display=swap" rel="stylesheet">
<style>
  :root {
    --orange: #f07800;
    --white: #ffffff;
    --light: #f1f1f1;
    --panel-top: #4b4b4b;
    --panel-bottom: #2b2b2b;
    --band: #4a4a4a;
    --ink: #333333;
    --rule: #c9c9c9;
    --quote: #b5b5b5;
  }
  * { box-sizing: border-box; margin: 0; padding: 0; }
  html, body { width: 990px; height: 1200px; overflow: hidden; background: var(--light); }
  .flyer { position: relative; width: 990px; height: 1200px; overflow: hidden; font-family: "Montserrat", sans-serif; }

  .hero-photo {
    position: absolute; left: 0; top: 0; width: 990px; height: 610px;
    background: linear-gradient(180deg, #d9d0c2 0%, #bdb3a4 35%, #8f877c 70%, #6f6a64 100%);
  }
  .shapes { position: absolute; left: 0; top: 0; width: 990px; height: 1200px; }

  .promise { position: absolute; left: 78px; top: 343px; height: 216px; border-left: 3px solid var(--white); padding-left: 29px; color: var(--white); font-family: "Barlow Condensed", sans-serif; }
  .promise .small { display: block; font-size: 37px; font-weight: 600; line-height: 40px; }
  .promise .big { display: block; font-size: 70px; font-weight: 700; line-height: 68px; }

  .badge { position: absolute; left: 654px; top: 343px; width: 252px; height: 252px; border-radius: 50%; background: var(--white); display: flex; align-items: center; justify-content: center; font-family: "Barlow Condensed", sans-serif; font-weight: 700; font-size: 44px; color: #1a1a1a; letter-spacing: 3px; }

  .services { position: absolute; left: 72px; top: 590px; width: 397px; height: 414px; border-radius: 16px 16px 0 16px; background: linear-gradient(180deg, var(--panel-top), var(--panel-bottom)); color: var(--white); }
  .services h2 { position: absolute; left: 27px; width: 290px; top: 28px; text-align: center; font-family: "Barlow Condensed", sans-serif; font-weight: 700; font-size: 50px; letter-spacing: 2px; line-height: 1; }
  .services .rule { position: absolute; left: 27px; top: 95px; width: 290px; height: 2px; background: var(--orange); }
  .service-list { list-style: none; position: absolute; left: 27px; top: 124px; width: 350px; font-family: "Barlow Semi Condensed", sans-serif; font-weight: 600; font-size: 25px; line-height: 30px; }
  .service-list li { position: relative; padding-left: 32px; margin-bottom: 16px; }
  .service-list li::before { content: "»"; position: absolute; left: 0; top: -3px; color: var(--orange); font-size: 32px; font-weight: 700; }

  .phone-bar { position: absolute; left: 72px; top: 1032px; width: 397px; height: 72px; background: var(--orange); display: flex; align-items: center; padding-left: 24px; gap: 12px; color: var(--white); font-family: "Barlow Condensed", sans-serif; font-weight: 700; font-size: 50px; }
  .contact-bar { position: absolute; left: 72px; top: 1104px; width: 397px; height: 45px; background: #222; display: flex; font-family: "Barlow", sans-serif; font-weight: 600; font-size: 15px; color: var(--white); }
  .contact-bar span { display: flex; align-items: center; justify-content: center; }
  .contact-bar .web { width: 200px; border-right: 2px solid #3d3d3d; }
  .contact-bar .mail { flex: 1; }

  .review { position: absolute; left: 552px; width: 366px; }
  .review .frame { position: absolute; left: 0; top: 26px; bottom: 10px; width: 1px; background: var(--rule); }
  .review .base { position: absolute; left: 0; bottom: 10px; height: 1px; background: var(--rule); }
  .review .open { position: absolute; left: 2px; top: -12px; font-family: "Barlow Condensed", sans-serif; font-weight: 700; font-size: 64px; color: var(--quote); line-height: 1; }
  .review .stars { position: absolute; right: 0; top: 4px; color: var(--orange); font-size: 12px; letter-spacing: 2px; }
  .review p { position: absolute; left: 20px; right: 0; top: 32px; font-size: 11.6px; line-height: 16px; color: var(--ink); text-align: justify; }
  .review .name { position: absolute; right: 38px; bottom: 0; font-weight: 600; font-size: 14px; color: var(--orange); background: var(--light); padding-left: 8px; }
  .review .close { position: absolute; right: 0; bottom: -28px; font-family: "Barlow Condensed", sans-serif; font-weight: 700; font-size: 64px; color: var(--quote); line-height: 1; }

  .social { position: absolute; left: 590px; top: 1120px; display: flex; align-items: center; gap: 10px; font-family: "Barlow", sans-serif; font-weight: 600; font-size: 17px; color: var(--white); }
  .social .dot { width: 16px; height: 16px; border-radius: 50%; background: #7a7a7a; }
</style>
</head>
<body>
<div class="flyer">
  <div class="hero-photo" role="img" aria-label="Photo of a bright modern interior with a chandelier, pot lights and recessed ceiling lighting"></div>

  <svg class="shapes" viewBox="0 0 990 1200" aria-hidden="true">
    <polygon points="529,610 990,408 990,1095 0,1095 0,610" fill="#f1f1f1"/>
    <polygon points="0,307 529,307 675,386 675,549 529,610 0,610" fill="#f07800"/>
    <rect x="0" y="1095" width="990" height="105" fill="#4a4a4a"/>
  </svg>

  <div class="promise">
    <span class="small">Our Promise is to</span>
    <span class="big">deliver the best</span>
    <span class="small">possible service</span>
    <span class="big">at fair prices!</span>
  </div>

  <div class="badge">VOLTARISA</div>

  <section class="services">
    <h2>OUR SERVICES</h2>
    <div class="rule"></div>
    <ul class="service-list">
      <li>LED Lighting Upgrades<br>(pot lights,<br>accent &amp; commercial)</li>
      <li>Electrical Repairs &amp;<br>Service work</li>
      <li>Fayglowen Lighting</li>
      <li>Tv Wall Mounts</li>
    </ul>
  </section>

  <div class="phone-bar">
    <svg width="40" height="40" viewBox="0 0 40 40" aria-hidden="true">
      <circle cx="20" cy="20" r="17.5" fill="none" stroke="#fff" stroke-width="3"/>
      <path d="M14 11c1.5-1 3-.5 3.6.8l1.2 2.6c.5 1 .2 2-.6 2.6l-1.2.9c.9 2.4 2.6 4.3 4.9 5.5l1-1.1c.7-.8 1.8-1 2.7-.4l2.4 1.5c1.2.8 1.4 2.3.5 3.6-1.1 1.6-3 2.3-4.9 1.6-5.3-2-9.1-6.1-10.6-11.5-.5-2 .2-4.1 1-6.1z" fill="#fff"/>
    </svg>
    <span>(555) 218-7306</span>
  </div>
  <div class="contact-bar">
    <span class="web">www.voltarisa.ca</span>
    <span class="mail">Devon@Voltarisa.ca</span>
  </div>

  <article class="review" style="top:634px;height:140px;">
    <div class="frame"></div><div class="base" style="width:230px;"></div>
    <span class="open">“</span><span class="stars">★★★★★</span>
    <p>Devon did some shop work for me and did a great job. Hooked up a couple of hoists and compressor in an old shop that had several renovations. He figured it out. Was very professional, punctual and fair. I would recommend him and will use him again.</p>
    <span class="name">Marlon Pettigrew</span><span class="close">”</span>
  </article>

  <article class="review" style="top:792px;height:86px;">
    <div class="frame"></div><div class="base" style="width:240px;"></div>
    <span class="open">“</span><span class="stars">★★★★★</span>
    <p>over all a very positive experience will definitely recommended and wont hesitate to use them again</p>
    <span class="name">Lena Ashcroft</span><span class="close">”</span>
  </article>

  <article class="review" style="top:897px;height:166px;">
    <div class="frame"></div><div class="base" style="width:225px;"></div>
    <span class="open">“</span><span class="stars">★★★★★</span>
    <p>Hired Devon to do some electrical in our home. Had two other electricians come in before him and neither could figure out how to do the job. Devon scoped it out very well and managed to get it all done with no issues. He was on time, kept a very clean work area, was quick, and very pleasant all around. Will be going to him for all our future electrical needs.</p>
    <span class="name">Corinne Vale</span><span class="close">”</span>
  </article>

  <div class="social">
    <span class="dot"></span>
    <span>/VoltarisaContracting/</span>
  </div>
</div>
</body>
</html>
```